BRH 2014 Seasons Greetings

Christmas postcards.
Side A: Image with 3 logos "Varek Cove Lodge" "Mirufa Lodge Samoa" "Keli Vasa"(Logos on bottom of card" & "Seasons Greetings" (to fit)
Side B Left:
Text
"Management and staff at Corvina Lodges wish you and your family a very happy and safe festive season and all the best for the New Year.
Counting down your next arrival"
Side B Right: Address template with 4 lines & Area for stamp top right corner.
Side B Base: Logo & Website "Corvina Lodges" " www.corvinalodges.example"
Target Market(s)
High end travel
Industry/Entity Type
Management
Look and feel
Each slider illustrates characteristics of the customer's brand and the style your logo design should communicate.

```html
<!DOCTYPE html>
<html lang="en">
<head>
<meta charset="utf-8">
<title>Corvina Lodges – Season's Greetings Postcard</title>
<link rel="stylesheet" href="https://fonts.googleapis.com/css2?family=Jost:wght@300;400;500&family=Open+Sans:wght@400&display=swap">
<style>
  :root {
    --backdrop: #e6a200;
    --card-white: #ffffff;
    --night: #050805;
    --palm-green: #2f7a48;
    --spark-orange: #e07a2a;
    --ink-grey: #9b9b9b;
    --rule-grey: #8e8e8e;
    --front-text: #ffffff;
  }
  html, body {
    margin: 0;
    padding: 0;
    width: 1200px;
    height: 770px;
    overflow: hidden;
    background: var(--backdrop);
  }
  .canvas {
    position: relative;
    width: 1200px;
    height: 770px;
  }

  /* Side A */
  .postcard-front {
    position: absolute;
    left: 72px;
    top: 59px;
    width: 454px;
    height: 586px;
    overflow: hidden;
    box-shadow: 4px 4px 6px rgba(0,0,0,0.35);
    background: var(--night);
  }
  .front-photo {
    position: absolute;
    inset: 0;
    background:
      radial-gradient(ellipse 55% 30% at 60% 38%, rgba(224,122,42,0.55), transparent 70%),
      radial-gradient(ellipse 35% 25% at 72% 68%, rgba(224,122,42,0.35), transparent 70%),
      radial-gradient(ellipse 45% 40% at 25% 35%, rgba(47,122,72,0.75), transparent 70%),
      radial-gradient(ellipse 40% 30% at 40% 70%, rgba(47,122,72,0.45), transparent 70%),
      linear-gradient(180deg, #030503 0%, #071008 70%, #1c2a22 100%);
  }
  .front-title {
    position: absolute;
    top: 40px;
    left: 0;
    width: 100%;
    margin: 0;
    text-align: center;
    font-family: "Jost", sans-serif;
    font-weight: 300;
    font-size: 25px;
    letter-spacing: 1.7px;
    color: var(--front-text);
  }
  .partner-lodges {
    position: absolute;
    left: 36px;
    bottom: 34px;
    margin: 0;
    padding: 0;
    list-style: none;
    font-family: "Open Sans", sans-serif;
    font-size: 8.5px;
    line-height: 11px;
    color: var(--front-text);
  }
  .partner-site {
    position: absolute;
    left: 34px;
    bottom: 14px;
    font-family: "Open Sans", sans-serif;
    font-size: 11.5px;
    color: var(--front-text);
  }
  .front-brand {
    position: absolute;
    right: 32px;
    bottom: 36px;
    font-family: "Jost", sans-serif;
    font-weight: 400;
    font-size: 10px;
    letter-spacing: 1.2px;
    color: var(--front-text);
  }

  /* Side B */
  .postcard-back {
    position: absolute;
    left: 554px;
    top: 194px;
    width: 584px;
    height: 454px;
    background: var(--card-white);
    box-shadow: 3px 3px 5px rgba(0,0,0,0.35);
  }
  .back-brand {
    position: absolute;
    right: 321px;
    top: 54px;
    font-family: "Jost", sans-serif;
    font-weight: 400;
    font-size: 11.5px;
    letter-spacing: 1.5px;
    color: var(--ink-grey);
    white-space: nowrap;
  }
  .greeting {
    position: absolute;
    left: 41px;
    top: 161px;
    width: 221px;
    font-family: "Open Sans", sans-serif;
    font-size: 12px;
    line-height: 16px;
    color: var(--ink-grey);
  }
  .greeting p { margin: 0 0 16px; }
  .greeting .message { text-align: justify; }
  .website {
    position: absolute;
    left: 40px;
    width: 223px;
    top: 388px;
    font-family: "Open Sans", sans-serif;
    font-size: 16px;
    letter-spacing: -0.1px;
    color: var(--ink-grey);
    white-space: nowrap;
    text-align: right;
  }
  .divider {
    position: absolute;
    left: 281px;
    top: 28px;
    width: 1px;
    height: 390px;
    background: var(--rule-grey);
  }
  .address-lines {
    position: absolute;
    left: 309px;
    top: 187px;
    width: 221px;
    margin: 0;
    padding: 0;
    list-style: none;
  }
  .address-lines li {
    height: 1px;
    background: var(--rule-grey);
    margin-bottom: 44px;
  }
  .address-lines li:first-child {
    margin-bottom: 49px;
  }
</style>
</head>
<body>
<main class="canvas">

  <section class="postcard-front" aria-label="Postcard side A">
    <div class="front-photo" role="img" aria-label="Night photograph of palm trees lit green with fireworks streaking orange and pink across a beach sky"></div>
    <h1 class="front-title">SEASON’S GREETINGS!</h1>
    <ul class="partner-lodges">
      <li>Varek Cove Lodge</li>
      <li>Mirufa Lodge Samoa</li>
      <li>Keli Vasa</li>
    </ul>
    <div class="partner-site">varekcovelodge.example</div>
    <div class="front-brand">CORVINA LODGES &amp; RESORTS</div>
  </section>

  <section class="postcard-back" aria-label="Postcard side B">
    <div class="back-brand">CORVINA LODGES &amp; RESORTS</div>
    <div class="greeting">
      <p class="message">Management and staff at Corvina Lodges wish you and your family a very happy and safe festive season and all the best for the New Year.</p>
      <p>Counting down your next arrival</p>
    </div>
    <div class="website">www.corvinalodges.example</div>
    <div class="divider"></div>
    <ul class="address-lines" aria-label="Address lines">
      <li></li>
      <li></li>
      <li></li>
      <li></li>
    </ul>
  </section>

</main>
</body>
</html>
```